Website Redesign - home improvements/garage door supplier & installer in London

We are a garage door specialist providing installation, automation and repair services throughout the South East England with 5 branches/showrooms across London and over 65 employees. Garage doors are our main area of expertise but we have other home improvement products in our range - front/entrance doors, internal doors, sliding and bi-fold patio doors; awnings and shading systems.

Our current website is quite boring and uninviting so we are looking to redesign and modernise the whole site to improve the user experience and flow.
Responsive, desktop and mobile friendly.

www.brightwellportals.example

Main pages to be templated:

Homepage
Category pages/list e.g. https://www.brightwellportals.example/garage-doors/
Basic content/product pages e.g https://www.brightwellportals.example/veltrop-internal-doors/
Main services pages e.g. https://www.brightwellportals.example/garage-door-installation/
Branch pages e.g. https://www.brightwellportals.example/branch-one/
Contact page
-----------------------
Our logo must stay as is (the attached AI file has 3 elements - logo -BRIGHTWELL PORTALS with the 'A'mark, the SINCE 1976 mark and a tagline 'Far beyond the everyday entrance' - these elements are to be used separately, not as a single block - although they can be combined)). Please use the text that’s already on the site in your design previews.
Our main colours are Blue RGB 35,57,119 and Red RGB 228,25,34

We would welcome a new smarter colour scheme but you will have to stick with the 2 primary colours we use on our logo - so any complimentary colours that might fit the new design would be great.

You can use all images that are on the website to support the new design - also attached is a zip with logo and images)

Target Market(s)

Most of our customers are in and around London - homeowners with garages that need servicing, replacing garage doors, upgrading or fitting new + other hiome improvements we can offer as listed above (fornt doors, bifold, sliding patio doors and awning) B2C

Industry/Entity Type

Home Improvement

Coding

Coded - Design and coding required

Font styles to use
Sans Serif

Requirements
Must have
• Custom and responsive design, user friendly, use our main 2 colours (red and blue described above) but add some complimentary colours to the mix
Nice to have
• Be creative, innovative
Should not have
• This should not be just some freely available wordpress template

```html
<!DOCTYPE html>
<html lang="en">
<head>
<meta charset="utf-8">
<title>Brightwell Portals – Garage Doors</title>
<link href="https://fonts.googleapis.com/css2?family=Raleway:ital,wght@0,500;0,700;0,800;1,600&family=Open+Sans:ital,wght@0,400;0,600;0,700;1,400&display=swap" rel="stylesheet">
<style>
:root{
  --blue:#233977;
  --blue-dark:#1a2b5c;
  --red:#e41922;
  --red-dark:#b8121a;
  --ink:#333;
  --grey:#777;
  --light:#f4f4f6;
  --line:#e2e2e6;
  --footer:#1e1e22;
  --footer-deep:#141417;
  --white:#fff;
}
*{box-sizing:border-box;margin:0;padding:0}
html,body{width:1200px;height:4959px;overflow:hidden}
body{font-family:"Open Sans",sans-serif;color:var(--ink);background:var(--white);position:relative}
.section{position:absolute;left:0;width:1200px}
h2.title{font-family:"Raleway",sans-serif;font-weight:800;font-size:36px;text-align:center;color:var(--red)}
.divider{display:flex;align-items:center;justify-content:center;gap:8px;margin:12px auto 0}
.divider span{display:block;width:60px;height:1px;background:currentColor;opacity:.5}
.divider i{display:block;width:8px;height:8px;border-radius:50%;background:currentColor}

/* top nav */
.topnav{top:0;height:63px;background:var(--blue);display:flex;justify-content:center;align-items:center}
.topnav a{color:var(--white);text-decoration:none;font-size:14px;font-weight:600;padding:0 18px;border-right:1px solid rgba(255,255,255,.35);letter-spacing:.3px}
.topnav a:last-child{border-right:0}

/* header */
.header{top:63px;height:119px;display:flex;align-items:center;padding:0 80px}
.brand{display:flex;align-items:center;gap:14px}
.brand-square{width:54px;height:54px;background:var(--red)}
.brand-name{font-family:"Raleway",sans-serif;font-weight:800;font-size:28px;color:var(--blue);line-height:1}
.brand-tag{font-size:13px;color:var(--blue);font-style:italic;margin-top:6px}
.since-badge{width:58px;height:58px;border-radius:50%;background:var(--blue);margin-left:16px}
.call{margin-left:auto;display:flex;align-items:center;gap:10px;font-family:"Raleway",sans-serif;font-weight:800;font-size:24px;color:var(--blue)}
.call b{color:var(--red)}
.search{display:flex;margin-left:36px}
.search span{width:128px;height:44px;border:1px solid var(--line);font-size:14px;color:#999;padding:12px}
.search button{width:40px;height:44px;border:0;background:var(--blue);display:flex;align-items:center;justify-content:center}

/* hero */
.hero{top:182px;height:684px;background:linear-gradient(100deg,#6b4c32 0%,#c9b79b 28%,#e8e2d6 48%,#9aa58a 70%,#57623f 100%)}
.hero-circle{position:absolute;left:360px;top:100px;width:462px;height:462px;border-radius:50%;background:rgba(228,25,34,.93);display:flex;flex-direction:column;align-items:center;justify-content:center;text-align:center;padding:0 60px}
.hero-circle h1{font-family:"Raleway",sans-serif;font-weight:700;font-size:34px;line-height:1.25;color:var(--white);margin-top:70px}
.hero-btns{display:flex;gap:14px;margin-top:30px}
.btn{display:inline-block;font-family:"Raleway",sans-serif;font-weight:700;font-size:15px;color:var(--white);padding:16px 24px;text-decoration:none;text-transform:uppercase;letter-spacing:.4px}
.btn-blue{background:var(--blue)}
.btn-red{background:var(--red)}
.btn-darkred{background:var(--red-dark);line-height:1.2;padding:10px 22px}

/* choose */
.choose{top:866px;height:572px}
.choose h2{margin-top:44px}
.choose .divider{color:var(--red)}
.choose p.lead{width:680px;margin:26px auto 0;text-align:center;font-size:14px;color:var(--grey);line-height:1.7}
.steps{display:flex;gap:12px;justify-content:center;margin-top:36px}
.step{width:254px;height:220px;border:1px solid var(--line);border-radius:12px;background:var(--white);box-shadow:0 3px 10px rgba(0,0,0,.06);position:relative;text-align:center;padding:40px 20px 0}
.step .num{position:absolute;right:16px;top:6px;font-family:"Raleway",sans-serif;font-weight:800;font-size:38px;color:#e7e9ef}
.step h3{font-family:"Raleway",sans-serif;font-weight:800;font-size:17px;color:var(--red);margin-top:10px}
.step p{font-size:13px;color:var(--grey);line-height:1.55;margin-top:8px}

/* about */
.about{top:1438px;height:519px;background:linear-gradient(135deg,var(--blue) 0%,#2c4a8f 55%,var(--blue-dark) 100%)}
.about h2{color:var(--white);margin-top:56px}
.about .divider{color:var(--white)}
.about-text{position:absolute;left:80px;top:160px;width:580px;color:var(--white);font-size:14px;line-height:1.65}
.ticks{display:grid;grid-template-columns:250px 250px;gap:18px 0;margin-top:26px}
.ticks li{list-style:none;display:flex;align-items:center;gap:14px;font-size:17px;font-weight:600}
.ticks li:before{content:"";width:12px;height:12px;background:var(--red);transform:rotate(45deg)}
.video{position:absolute;left:686px;top:160px;width:438px;height:290px;background:linear-gradient(160deg,#b8c3cf 0%,#e6e3dc 40%,#8d8a7f 100%);border:4px solid rgba(255,255,255,.85)}
.play{position:absolute;left:190px;top:116px;width:58px;height:58px;border-radius:50%;background:var(--red);display:flex;align-items:center;justify-content:center}

/* services */
.services{top:1957px;height:678px}
.services h2{margin-top:62px}
.services .divider{color:var(--red)}
.service-row{display:flex;justify-content:center;gap:84px;margin-top:50px}
.service{width:270px;position:relative;height:250px}
.service .photo{width:222px;height:222px;border-radius:50%;margin:0 auto;border:6px solid var(--white);box-shadow:0 4px 14px rgba(0,0,0,.15)}
.ribbon{position:absolute;left:0;top:170px;width:270px;height:44px;background:var(--red);color:var(--white);font-family:"Raleway",sans-serif;font-weight:700;font-size:16px;display:flex;align-items:center;justify-content:center;clip-path:polygon(0 0,100% 0,94% 50%,100% 100%,0 100%,6% 50%)}
.services p{width:620px;margin:46px auto 0;text-align:center;font-size:14px;color:var(--grey);line-height:1.7}
.services .cta{text-align:center;margin-top:28px}

/* reviews */
.reviews{top:2635px;height:638px;background:linear-gradient(180deg,#e8333a 0%,var(--red) 50%,#d0141c 100%)}
.reviews h2{color:var(--white);margin-top:60px}
.reviews .divider{color:var(--white)}
.review-row{display:flex;justify-content:center;gap:53px;margin-top:30px}
.review{width:310px;height:347px;background:var(--white);border-radius:6px;text-align:center;padding:24px 26px;box-shadow:0 6px 18px rgba(0,0,0,.18)}
.stars{display:flex;justify-content:center;gap:3px}
.review h4{font-family:"Raleway",sans-serif;font-style:italic;font-weight:600;font-size:18px;color:var(--blue);line-height:1.35;margin-top:10px}
.review blockquote{font-size:13px;font-style:italic;color:var(--grey);line-height:1.6;margin-top:28px}
.review .who{font-family:"Raleway",sans-serif;font-weight:700;font-size:14px;color:var(--red);margin-top:30px}
.dots{display:flex;justify-content:center;gap:10px;margin-top:44px}
.dots i{width:14px;height:14px;border-radius:50%;border:2px solid var(--white)}
.dots i.on{background:var(--white)}

/* also offers */
.offers{top:3273px;height:690px}
.offers h2{margin-top:94px}
.offers .divider{color:var(--red)}
.offer-row{display:flex;justify-content:center;gap:44px;margin-top:50px}
.offer{width:230px;text-align:center}
.offer .photo{width:226px;height:226px;border-radius:50%;margin:0 auto;border:6px solid var(--white);box-shadow:0 4px 14px rgba(0,0,0,.15)}
.offer h5{font-family:"Raleway",sans-serif;font-weight:700;font-size:17px;color:var(--blue);margin-top:18px}
.offers .cta{text-align:center;margin-top:42px}
.partners{display:flex;justify-content:center;gap:30px;margin-top:40px}
.partners span{width:112px;height:32px;background:#d6d9e2;border-radius:3px}
.partners span:nth-child(odd){background:#e7c9cb}

/* contact */
.contact{top:3963px;height:368px;background:var(--light)}
.contact h2{margin-top:56px}
.contact .divider{color:var(--red)}
.form{position:absolute;left:205px;top:172px;display:grid;grid-template-columns:215px 210px 220px 106px;grid-template-rows:52px 52px;gap:18px 12px}
.field{background:var(--white);border:1px solid var(--line);font-size:13px;color:#999;padding:16px 14px}
.field.msg{grid-column:3;grid-row:1 / span 2}
.submit{grid-column:4;grid-row:1 / span 2;background:var(--blue);color:var(--white);border:0;font-family:"Raleway",sans-serif;font-weight:700;font-size:15px}

/* footer */
.footer{top:4331px;height:568px;background:var(--footer);color:#c9c9cf}
.fcol{position:absolute;top:70px}
.fcol h6{font-family:"Raleway",sans-serif;font-weight:800;font-size:16px;color:var(--white);margin-bottom:22px}
.fcol li{list-style:none;font-size:13px;line-height:29px}
.fcontact{position:absolute;left:910px;top:0;width:290px;height:568px;background:var(--footer-deep);padding:70px 24px 0}
.fcontact h6{font-family:"Raleway",sans-serif;font-weight:800;font-size:16px;color:var(--white);margin-bottom:22px}
.fcontact p{font-size:13px;line-height:22px;color:#c9c9cf}
.fcontact strong{color:var(--white);font-size:12px}
.fcontact .gap{margin-top:14px}
.bottom{top:4899px;height:60px;background:var(--red);display:flex;justify-content:center;align-items:center;gap:10px}
.bottom i{width:30px;height:30px;border-radius:50%;background:var(--white)}
</style>
</head>
<body>

<nav class="section topnav">
  <a>HOME</a><a>OUR PRODUCTS</a><a>INSTALLATIONS</a><a>REPAIRS</a><a>SPECIAL OFFERS</a><a>TESTIMONIALS</a><a>CONTACT US</a><a>CAREERS</a>
</nav>

<header class="section header">
  <div class="brand">
    <div class="brand-square"></div>
    <div>
      <div class="brand-name">BRIGHTWELL PORTALS</div>
      <div class="brand-tag">Far beyond the everyday entrance</div>
    </div>
    <div class="since-badge"></div>
  </div>
  <div class="call">
    <svg width="24" height="24" viewBox="0 0 24 24"><path fill="#233977" d="M6.6 10.8a15.1 15.1 0 0 0 6.6 6.6l2.2-2.2c.3-.3.7-.4 1-.2 1.1.4 2.3.6 3.6.6.6 0 1 .4 1 1V20c0 .6-.4 1-1 1A17 17 0 0 1 3 4c0-.6.4-1 1-1h3.5c.6 0 1 .4 1 1 0 1.3.2 2.5.6 3.6.1.3 0 .7-.2 1z"/></svg>
    CALL US : <b>0800 555 0142</b>
  </div>
  <div class="search">
    <span>Search...</span>
    <button aria-label="Search"><svg width="16" height="16" viewBox="0 0 16 16"><circle cx="6.5" cy="6.5" r="5" fill="none" stroke="#fff" stroke-width="2"/><path d="M10.5 10.5 15 15" stroke="#fff" stroke-width="2"/></svg></button>
  </div>
</header>

<section class="section hero" role="img" aria-label="Kitchen interior opening through folding glass doors onto a garden patio">
  <div class="hero-circle">
    <h1>It was great to meet you at the Home Build Expo</h1>
    <div class="hero-btns">
      <a class="btn btn-blue">Get in touch</a>
      <a class="btn btn-darkred">Book your<br>free survey</a>
    </div>
  </div>
</section>

<section class="section choose">
  <h2 class="title">We'll help you Choose the right door</h2>
  <div class="divider"><span></span><i></i><span></span></div>
  <p class="lead">You may have started looking for a new garage door for a number of reasons. Whether your garage door may be broken or you simply want to improve the look of your house.</p>
  <div class="steps">
    <div class="step"><span class="num">01</span>
      <svg width="40" height="36" viewBox="0 0 40 36"><path fill="#233977" d="M20 2 2 18h5v16h10V24h6v10h10V18h5z"/></svg>
      <h3>WHAT YOU NEED</h3><p>Tell us your requirements - our products can be designed especially for you</p></div>
    <div class="step"><span class="num">02</span>
      <svg width="34" height="38" viewBox="0 0 34 38"><rect x="3" y="5" width="28" height="31" rx="3" fill="#233977"/><rect x="11" y="1" width="12" height="8" rx="2" fill="#233977" stroke="#fff" stroke-width="2"/><path d="M9 17h16M9 23h16M9 29h10" stroke="#fff" stroke-width="2.5"/></svg>
      <h3>YOUR SURVEY</h3><p>Our trained surveyor will measure up and evaluate the work required</p></div>
    <div class="step"><span class="num">03</span>
      <svg width="40" height="38" viewBox="0 0 40 38"><rect x="2" y="10" width="36" height="26" rx="3" fill="#233977"/><rect x="13" y="4" width="14" height="8" rx="2" fill="none" stroke="#233977" stroke-width="3"/><text x="20" y="30" fill="#fff" font-family="Open Sans,sans-serif" font-weight="700" font-size="16" text-anchor="middle">£</text></svg>
      <h3>QUOTATION</h3><p>After your survey, we'll provide you with a quote for the job and then you can complete your purchase</p></div>
    <div class="step"><span class="num">04</span>
      <svg width="36" height="38" viewBox="0 0 36 38"><path fill="#233977" d="M6 14a12 12 0 0 1 24 0z"/><rect x="4" y="13" width="28" height="3" fill="#233977"/><circle cx="18" cy="21" r="6" fill="#233977"/><path fill="#233977" d="M4 38c0-8 6-12 14-12s14 4 14 12z"/></svg>
      <h3>INSTALLATION</h3><p>Our fully trained specialist installer will fit or repair your door on a day that suits you</p></div>
  </div>
</section>

<section class="section about">
  <h2 class="title">Brightwell Portals</h2>
  <div class="divider"><span></span><i></i><span></span></div>
  <div class="about-text">
    <p>Here at Brightwell Portals we've been putting our customers first for 40 years, providing thousands of garage doors throughout London and the South East. We work directly with leading manufacturers to bring you a premium garage door installation and repair facility. Our fully trained professional garage door installers and engineers provide friendly advice and a reliable service.</p>
    <ul class="ticks">
      <li>Friendly helpful advice</li><li>Fully trained installers</li>
      <li>FREE Estimates*</li><li>Satisfaction guaranteed</li>
      <li>Affordable prices</li>
    </ul>
  </div>
  <div class="video" role="img" aria-label="Video still of a white up-and-over garage door beside a parked car">
    <div class="play"><svg width="22" height="24" viewBox="0 0 22 24"><path d="M3 2l17 10L3 22z" fill="#fff"/></svg></div>
  </div>
</section>

<section class="section services">
  <h2 class="title">Unrivalled Service at affordable prices</h2>
  <div class="divider"><span></span><i></i><span></span></div>
  <div class="service-row">
    <div class="service"><div class="photo" role="img" aria-label="Close view of a white sectional garage door" style="background:linear-gradient(150deg,#7fa3c9,#e9edf1 55%,#b7bcc3)"></div><div class="ribbon">GARAGE DOOR TYPES</div></div>
    <div class="service"><div class="photo" role="img" aria-label="Brick house with a timber bifold garage door" style="background:linear-gradient(160deg,#9cc0e2,#c47b4f 55%,#8a5a3c)"></div><div class="ribbon">BIFOLD DOORS</div></div>
    <div class="service"><div class="photo" role="img" aria-label="Engineer repairing a garage door mechanism" style="background:linear-gradient(150deg,#d7d4cd,#8e8b83 55%,#4f4c48)"></div><div class="ribbon">GARAGE DOOR REPAIRS</div></div>
  </div>
  <p>At Brightwell Portals we pride ourselves on knowledgeable, friendly staff who will assist you in choosing the best automatic garage doors to suit your property and budget.</p>
  <div class="cta"><a class="btn btn-blue">Find a showroom</a></div>
</section>

<section class="section reviews" role="img" aria-label="Red tinted band of customer portraits behind the reviews">
  <h2 class="title">Customer Reviews</h2>
  <div class="divider"><span></span><i></i><span></span></div>
  <div class="review-row">
    <div class="review">
      <div class="stars"><svg width="100" height="18" viewBox="0 0 100 18"><g fill="#f2b01e"><path id="st" d="M9 1l2.4 5 5.5.7-4 3.8 1 5.5L9 13.4 4.1 16l1-5.5-4-3.8 5.5-.7z"/><use href="#st" x="20"/><use href="#st" x="40"/><use href="#st" x="60"/></g><use href="#st" x="80" fill="none" stroke="#f2b01e"/></svg></div>
      <h4>Supply and fit new garage up-over door</h4>
      <blockquote>" Friendly and courteous service, promptness, supplying estimates and keeping to dates agreed"</blockquote>
      <div class="who">Customer in Brackenford 10/10</div>
    </div>
    <div class="review">
      <div class="stars"><svg width="100" height="18" viewBox="0 0 100 18"><g fill="#f2b01e"><use href="#st"/><use href="#st" x="20"/><use href="#st" x="40"/><use href="#st" x="60"/></g><use href="#st" x="80" fill="none" stroke="#f2b01e"/></svg></div>
      <h4>Supply and fit roller door and take away old up-and-over door</h4>
      <blockquote>" Both the surveyor and fitter did an excellent job. Very satisfied with their work."</blockquote>
      <div class="who">Customer in Hollowmere 10/10</div>
    </div>
    <div class="review">
      <div class="stars"><svg width="100" height="18" viewBox="0 0 100 18"><g fill="#f2b01e"><use href="#st"/><use href="#st" x="20"/><use href="#st" x="40"/><use href="#st" x="60"/></g><use href="#st" x="80" fill="none" stroke="#f2b01e"/></svg></div>
      <h4>Garage Door delivery and fitting</h4>
      <blockquote>" The delivery and fitting man was excellent, very polite tidy and the he done the best he could to make it fit well very helpful."</blockquote>
      <div class="who">Customer in Wrenfield 10/10</div>
    </div>
  </div>
  <div class="dots"><i></i><i class="on"></i><i></i></div>
</section>

<section class="section offers">
  <h2 class="title">We Also Offers</h2>
  <div class="divider"><span></span><i></i><span></span></div>
  <div class="offer-row">
    <div class="offer"><div class="photo" role="img" aria-label="Dark framed glazed front doors" style="background:linear-gradient(160deg,#dfe3e6,#5c5f63 55%,#2d2f32)"></div><h5>FRONT DOORS</h5></div>
    <div class="offer"><div class="photo" role="img" aria-label="Grey weatherproof garage door on a modern house" style="background:linear-gradient(160deg,#a9c6e4,#6d727b 55%,#3b3f46)"></div><h5>WEATHERPROOF DOORS</h5></div>
    <div class="offer"><div class="photo" role="img" aria-label="Retractable sun awning over a patio" style="background:linear-gradient(160deg,#f3e0c4,#c58a4e 55%,#7b5233)"></div><h5>SUN AWNINGS</h5></div>
    <div class="offer"><div class="photo" role="img" aria-label="White front door with canopy" style="background:linear-gradient(160deg,#f4f4f4,#cfd1d3 55%,#8e9194)"></div><h5>GARAGE DOOR SPARES</h5></div>
  </div>
  <div class="cta"><a class="btn btn-red">View all</a></div>
  <div class="partners"><span></span><span></span><span></span><span></span><span></span><span></span><span></span></div>
</section>

<section class="section contact">
  <h2 class="title">Contact Us</h2>
  <div class="divider"><span></span><i></i><span></span></div>
  <div class="form">
    <div class="field">Name :</div>
    <div class="field">Phone :</div>
    <div class="field msg">Message :</div>
    <button class="submit">SUBMIT</button>
    <div class="field">Email :</div>
    <div class="field">Address :</div>
  </div>
</section>

<footer class="section footer">
  <div class="fcol" style="left:80px"><h6>GARAGE DOORS</h6><ul><li>Garage Doors</li><li>Mechanism</li><li>Download a Brochure</li><li>Garage Door Photo Gallery</li><li>Stock List</li><li>Double Garage Door</li><li>Conversion</li></ul></div>
  <div class="fcol" style="left:292px"><h6>GUIDES</h6><ul><li>How to Order</li><li>Choose The Door For You</li><li>Download a Brochure</li><li>Installation</li><li>Garage Door Repairs</li><li>Blog</li></ul></div>
  <div class="fcol" style="left:506px"><h6>HELPFUL LINKS</h6><ul><li>About Us</li><li>Testimonials</li><li>FAQs</li><li>Request a Free Survey</li><li>Terms &amp; Conditions</li><li>Privacy Statement</li><li>Careers</li><li>Accreditations &amp; Certificates</li><li>Questionnaire</li><li>Trade Garage Doors</li><li>Garage Doors Spares</li><li>Garage Door Seal</li></ul></div>
  <div class="fcol" style="left:720px"><h6>SHOWROOMS</h6><ul><li>Garage Door Showrooms</li><li>Northbrook</li><li>Eastmere</li><li>Fernleigh</li><li>Oakhaven</li><li>Westcombe</li></ul></div>
  <div class="fcontact">
    <h6>CONTACT US</h6>
    <p><strong>HEAD OFFICE ADDRESS</strong></p>
    <p><b>A</b> - Larchmere House, Fenwick Way, Larchfield LF1 0ZZ</p>
    <p class="gap"><b>P</b> - 0800 555 0142</p>
    <p><b>E</b> - hello@brightwellportals.example</p>
    <p class="gap"><strong>OPENING HOURS</strong></p>
    <p><strong>MON - FRI</strong></p>
    <p>07:30 AM - 5:00 PM</p>
    <p><strong>SAT</strong></p>
    <p>09:00 AM - 12:30 PM</p>
  </div>
</footer>

<div class="section bottom"><i></i><i></i><i></i><i></i><i></i><i></i><i></i><i></i></div>

</body>
</html>
```